The Nine Gates for Tablet Reliance - Contemporary Book Cover Design

The Nine Gates for Tablet Reliance was published in March 2019 and is available on Brimora and other platforms now. However, I am not happy with the cover.  It's a good design in some ways - I thought it would stand out and be easily recognizable. But I don't really like the color scheme and feel that a self-help book should probably use some lighter colors and that the red is too strident. The color scheme carries over into other marketing materials like the website, social media, etc. and I don't like the red and black scheme for these purposes.
It's not essential that the cover contain an endorsement like the current one but it could. Here are some endorsements:
“A must-read for anyone who is addicted to or thinks they may have a problem with digital technology. This eloquent work will also be useful to academics and clinicians exploring potential solutions. The author recognizes the similarities between smartphone addiction and other addictions, and logically applies one of the most effective known solutions for addiction - The Nine Gates.”
-- Dale Wickersham: Noted Interventionist, Keynote Speaker and Addiction Visionary
“If you suffer from digital addiction, I strongly encourage you to use this book as your road map to get you back to the real world.”
-- Thomas Quillard, Founder of Online Channel Monitor.
The back cover would have the new design / color scheme, but can have similar text, bio, author image, etc. Or we could include the endorsements there and shorten the other text.
As for the cover it could be stylized, or an image, a partial image, or whatever. I am open to suggestions. Think about what would be inviting for a person searching for help with moderating their smartphone use.
Let's add a subtitle as well "An Inner Journey to Balanced Tablet Habits"
Here is a link to the book:
https://www.brimora.example/Nine-Gates-Tablet-Reliance/dp/4086213590

Target Market(s)
General, since this issue affects almost everyone.
Colors
Designer to choose colors to be used in the design.
Look and feel

```html
<!DOCTYPE html>
<html lang="en">
<head>
<meta charset="utf-8">
<title>The Nine Gates for Tablet Reliance — Book Cover</title>
<link rel="stylesheet" href="https://fonts.googleapis.com/css2?family=Montserrat:wght@400;600;700;800&display=swap">
<style>
  :root {
    --cover-bg: #fde9d8;
    --ink: #1c1c1c;
    --accent-rule: #f6b431;
    --art-steel: #a9c3cb;
    --art-teal: #3f7580;
    --art-hair: #e39a4c;
    --art-skin: #f6c9a6;
    --art-top: #d8322f;
  }
  * { margin: 0; padding: 0; box-sizing: border-box; }
  html, body {
    width: 753px;
    height: 1200px;
    overflow: hidden;
    background: var(--cover-bg);
  }
  .book-cover {
    position: relative;
    width: 753px;
    height: 1200px;
    background: var(--cover-bg);
    font-family: "Montserrat", sans-serif;
    color: var(--ink);
    overflow: hidden;
  }
  .subtitle {
    position: absolute;
    top: 26px;
    left: 0;
    width: 100%;
    text-align: center;
    font-size: 15px;
    font-weight: 600;
    letter-spacing: 1.6px;
    text-transform: uppercase;
  }
  .title {
    position: absolute;
    top: 125px;
    left: 0;
    width: 100%;
    text-align: center;
    font-size: 58px;
    font-weight: 700;
    line-height: 83px;
    letter-spacing: 5px;
    text-transform: uppercase;
  }
  .title-rule {
    position: absolute;
    top: 392px;
    left: 45px;
    width: 663px;
    height: 5px;
    background: var(--accent-rule);
  }
  .author {
    position: absolute;
    top: 436px;
    left: 221px;
    font-size: 14px;
    font-weight: 700;
    letter-spacing: 1.4px;
    text-transform: uppercase;
  }
  .cover-art {
    position: absolute;
    left: 50px;
    top: 482px;
    width: 678px;
    height: 718px;
  }
</style>
</head>
<body>
  <main class="book-cover">
    <p class="subtitle">“An Inner Journey to Balanced Tablet Habits”</p>
    <h1 class="title">The Nine Gates<br>for Tablet<br>Reliance</h1>
    <div class="title-rule"></div>
    <p class="author">By Jonas Selwick</p>
    <svg class="cover-art" viewBox="0 0 678 718" role="img"
         aria-label="Pop-art illustration of a woman whose eyes are covered by a tablet gripped by mechanical cables wrapped around her head and neck">
      <defs>
        <linearGradient id="artTone" x1="0" y1="0" x2="0" y2="1">
          <stop offset="0" stop-color="var(--art-steel)"/>
          <stop offset="0.32" stop-color="var(--art-teal)"/>
          <stop offset="0.55" stop-color="var(--art-hair)"/>
          <stop offset="0.78" stop-color="var(--art-skin)"/>
          <stop offset="0.9" stop-color="var(--art-top)"/>
          <stop offset="1" stop-color="var(--art-top)"/>
        </linearGradient>
      </defs>
      <rect x="0" y="0" width="678" height="760" rx="40" fill="url(#artTone)"/>
    </svg>
  </main>
</body>
</html>
```